The Quiet Hinge Mending Ledger

I am making a journal for tracking pain symptoms for TMJ (Jaw) pain. I have the cover designed and I just need the journal page designed that will repeat throughout the journal. The journal is the image on the left of the bundle. The page I would like to be developed is the picture that I hand sketched out. It should be a 6 x 9 page, similar to the attached example. Greyscale, no color. Thank you!

Target Market(s)

20-55 year old women

Industry/Entity Type

Healthcare

Colors

Designer to choose only greyscale colors for use in the design.

Requirements
Must have
• A neat, well-designed page with the content I have sketched out by hand.
Nice to have
• Creative display of the content I provided and development of the pain scale and pain diagram faces in a professional looking way.

```html
<!DOCTYPE html>
<html lang="en">
<head>
<meta charset="utf-8">
<title>The Quiet Hinge Mending Ledger – Daily Page</title>
<link href="https://fonts.googleapis.com/css2?family=Jost:wght@300;400;500&family=Roboto+Condensed:wght@400&display=swap" rel="stylesheet">
<style>
  :root{
    --backdrop:#d9d9d9;
    --paper:#ffffff;
    --band:#f1f1f2;
    --band-dark:#dcdcde;
    --row:#e4e4e6;
    --ink:#1e1e1e;
    --ink-soft:#444;
    --rule:#2a2a2a;
    --accent:#2a6db5;
    --spot:#e9a3b0;
  }
  *{box-sizing:border-box;margin:0;padding:0}
  html,body{width:1200px;height:1200px;overflow:hidden}
  body{background:var(--backdrop);font-family:"Jost",sans-serif;color:var(--ink)}
  .page{position:absolute;left:213px;top:20px;width:774px;height:1160px;background:var(--paper);box-shadow:0 4px 18px rgba(0,0,0,.18)}
  .block{position:absolute;left:22px;width:729px}
  .band{background:var(--band)}
  .band-dark{background:var(--band-dark)}
  .heading{font-weight:500;font-size:19px;text-align:center;letter-spacing:.3px}

  /* date row */
  .date-row{top:21px;height:51px;display:flex;align-items:center;padding:0 22px;font-weight:300;font-size:16px;gap:8px}
  .date-row .line{flex:1;border-bottom:1px solid var(--rule);height:14px;margin-right:18px}
  .date-row .line:last-child{margin-right:0}

  /* time table */
  .time{top:72px;height:186px}
  .time .heading{padding-top:8px}
  .time-table{position:absolute;left:19px;top:37px;width:692px;height:135px;border-collapse:collapse;background:var(--paper);font-weight:300;font-size:16px}
  .time-table td{border:1.5px solid var(--rule);text-align:left;padding-left:20px;height:33px}
  .time-table td.num{text-align:center;padding-left:0}
  .time-table tr:first-child td{height:34px}

  /* severity */
  .sev-title{top:258px;height:40px;line-height:42px}
  .sev-scale{top:298px;height:41px;display:flex;align-items:center}
  .sev-num{position:absolute;top:5px;width:31px;height:31px;border:2px solid var(--ink);border-radius:50%;font-size:17px;font-weight:500;display:flex;align-items:center;justify-content:center}
  .sev-faces{top:339px;height:91px}
  .face{position:absolute;top:3px;width:49px;height:49px;border-radius:50%;background:radial-gradient(circle at 40% 35%,#e8e8e8,#9a9a9a)}
  .face-label{position:absolute;top:56px;width:90px;text-align:center;font-family:"Roboto Condensed",sans-serif;font-size:14px;line-height:16px}

  /* location */
  .loc-title{top:430px;height:44px;line-height:46px}
  .loc-art{position:absolute;top:483px;height:81px;border-radius:30px 30px 14px 14px;background:radial-gradient(circle at 55% 45%,var(--spot) 0 12%,#e6e6e6 30%,#cfcfcf)}
  .loc-art.teeth{border-radius:14px;background:linear-gradient(#3a3a3a,#1d1d1d)}
  .loc-label{position:absolute;top:592px;font-size:19px;font-weight:500;letter-spacing:.3px}
  .status-box{position:absolute;left:499px;top:479px;width:253px;height:147px;border:1px solid #9a9a9a;background:var(--paper)}
  .status-box .group{position:absolute;left:15px;color:var(--accent);font-weight:500;font-size:17px;line-height:21px}
  .status-list{position:absolute;left:117px;top:4px;width:128px}
  .status-list li{list-style:none;height:22.5px;display:flex;align-items:center;gap:9px;font-size:16px;padding-left:5px}
  .status-list li:nth-child(odd){background:var(--row)}

  .box{display:inline-block;width:14px;height:14px;border:1.3px solid var(--ink-soft);background:var(--paper);flex:none}

  /* checklists */
  .list-title{height:40px;line-height:42px}
  .triggers-title{top:631px}
  .relief-title{top:839px}
  .checklist{position:absolute;top:0;display:flex;flex-direction:column;gap:0}
  .checklist li{list-style:none;height:28px;margin-bottom:0;display:flex;align-items:center;gap:15px;padding-left:12px;font-size:16px;letter-spacing:.3px;background:var(--row);border-bottom:1px solid var(--paper)}
  .fill{display:inline-block;width:120px;border-bottom:1px solid var(--rule);height:14px}
  .triggers{top:672px;height:112px;left:0;width:774px}
  .relief{top:877px;height:112px;left:0;width:774px}

  .body-state{position:absolute;left:44px;font-size:16px;letter-spacing:.3px;display:flex;align-items:center;gap:8px}

  /* notes */
  .notes-title{top:993px;height:41px;line-height:43px}
  .note-line{position:absolute;left:24px;width:727px;border-top:1px solid var(--rule)}
</style>
</head>
<body>
<main class="page">

  <section class="block band date-row">
    <span>Date</span><span class="line"></span>
    <span>Day of the Week</span><span class="line"></span>
  </section>

  <section class="block band-dark time">
    <h2 class="heading">TIME</h2>
    <table class="time-table">
      <tr><td style="width:49px"></td><td style="width:80px">Begin</td><td style="width:74px">End</td><td style="width:132px">Duration</td><td style="width:42px"></td><td style="width:86px">Begin</td><td style="width:77px">End</td><td>Duration</td></tr>
      <tr><td class="num">1</td><td></td><td></td><td></td><td class="num">4</td><td></td><td></td><td></td></tr>
      <tr><td class="num">2</td><td></td><td></td><td></td><td class="num">5</td><td></td><td></td><td></td></tr>
      <tr><td class="num">3</td><td></td><td></td><td></td><td class="num">6</td><td></td><td></td><td></td></tr>
    </table>
  </section>

  <h2 class="block band heading sev-title">SEVERITY OF PAIN (circle range)</h2>
  <section class="block band-dark sev-scale">
    <span class="sev-num" style="left:31px">1</span>
    <span class="sev-num" style="left:102px">2</span>
    <span class="sev-num" style="left:172px">3</span>
    <span class="sev-num" style="left:243px">4</span>
    <span class="sev-num" style="left:313px">5</span>
    <span class="sev-num" style="left:383px">6</span>
    <span class="sev-num" style="left:454px">7</span>
    <span class="sev-num" style="left:524px">8</span>
    <span class="sev-num" style="left:595px">9</span>
    <span class="sev-num" style="left:665px">10</span>
  </section>
  <section class="block sev-faces">
    <span class="face" role="img" aria-label="Mild pain face icon" style="left:93px"></span>
    <span class="face-label" style="left:72px">Mild</span>
    <span class="face" role="img" aria-label="Moderate pain face icon" style="left:234px"></span>
    <span class="face-label" style="left:213px">Moderate</span>
    <span class="face" role="img" aria-label="Severe pain face icon" style="left:374px"></span>
    <span class="face-label" style="left:353px">Severe</span>
    <span class="face" role="img" aria-label="Very severe pain face icon" style="left:515px"></span>
    <span class="face-label" style="left:494px">Very Severe</span>
    <span class="face" role="img" aria-label="Worst pain possible face icon" style="left:656px"></span>
    <span class="face-label" style="left:635px;top:50px">Worst Pain<br>Possible</span>
  </section>

  <h2 class="block band heading loc-title">LOCATION</h2>
  <div class="loc-art" role="img" aria-label="Head profile marking jaw joint pain" style="left:36px;width:73px"></div>
  <div class="loc-art" role="img" aria-label="Head profile marking muscle pain areas" style="left:125px;width:72px"></div>
  <div class="loc-art" role="img" aria-label="Head profile marking neck pain" style="left:217px;width:72px"></div>
  <div class="loc-art" role="img" aria-label="Front head view marking tension area" style="left:317px;width:59px"></div>
  <div class="loc-art teeth" role="img" aria-label="Teeth illustration" style="left:390px;width:88px;top:497px;height:54px"></div>
  <span class="loc-label" style="left:49px">Joint</span>
  <span class="loc-label" style="left:131px">Muscles</span>
  <span class="loc-label" style="left:241px">Neck</span>
  <span class="loc-label" style="left:309px">Tension</span>
  <span class="loc-label" style="left:409px">Teeth</span>
  <div class="status-box">
    <span class="group" style="top:25px">Click/Pop</span>
    <span class="group" style="top:77px">Opening<br>Ability</span>
    <ul class="status-list">
      <li><span class="box"></span>Increased</li>
      <li><span class="box"></span>Decreased</li>
      <li><span class="box"></span>No Change</li>
      <li><span class="box"></span>Incresed</li>
      <li><span class="box"></span>Decreased</li>
      <li><span class="box"></span>No Change</li>
    </ul>
  </div>

  <h2 class="block band heading list-title triggers-title">TRIGGERS (Check all that apply)</h2>
  <section class="block triggers">
    <ul class="checklist" style="left:27px;width:221px">
      <li><span class="box"></span>Sleep</li>
      <li><span class="box"></span>Frist thing in AM</li>
      <li><span class="box"></span>Clenching</li>
      <li><span class="box"></span>Insomnia</li>
    </ul>
    <ul class="checklist" style="left:257px;width:243px">
      <li><span class="box"></span>Weather</li>
      <li><span class="box"></span>Eating</li>
      <li><span class="box"></span>Work</li>
      <li><span class="box"></span>Opening Wild/yown</li>
    </ul>
    <ul class="checklist" style="left:507px;width:243px">
      <li><span class="box"></span>PMS/Menstration</li>
      <li><span class="box"></span>Stress at Home</li>
      <li><span class="box"></span>Stress at Work</li>
      <li><span class="box"></span>Othet <span class="fill" style="width:130px"></span></li>
    </ul>
  </section>
  <p class="body-state" style="top:786px">My Jaw was <span class="box"></span> relaxed <span class="box"></span> clenched <span class="box"></span> my breathing was <span class="box"></span> shallow/tense</p>
  <p class="body-state" style="top:810px">My neck/Shoulders were <span class="box"></span> relaxed <span class="box"></span> tense</p>

  <h2 class="block band heading list-title relief-title">Relief Measures (Check all that apply)</h2>
  <section class="block relief">
    <ul class="checklist" style="left:25px;width:243px">
      <li><span class="box"></span>Deep Breathing</li>
      <li><span class="box"></span>Teeth apart/Relax Jaw</li>
      <li><span class="box"></span>Self-Massage</li>
      <li><span class="box"></span>Heat/Cold (Circle)</li>
    </ul>
    <ul class="checklist" style="left:277px;width:242px">
      <li><span class="box"></span>Medication</li>
      <li><span class="box"></span>Rest</li>
      <li><span class="box"></span>Gentle Stretching</li>
      <li><span class="box"></span>Posture Correction</li>
    </ul>
    <ul class="checklist" style="left:527px;width:223px">
      <li><span class="box"></span>Mindful rest</li>
      <li><span class="box"></span>Stabilization Exercise</li>
      <li><span class="box"></span>Other <span class="fill" style="width:117px"></span></li>
      <li><span class="box"></span><span class="fill" style="width:165px"></span></li>
    </ul>
  </section>

  <h2 class="block band heading notes-title">Notes and Plan to Avoid Triggevs</h2>
  <div class="note-line" style="top:1064px"></div>
  <div class="note-line" style="top:1098px"></div>
  <div class="note-line" style="top:1130px"></div>

</main>
</body>
</html>
```